Orlent Telecom Business Card Competition

High quality international communications for consumers and business. We are re-designing our website and re-branding. Our current (old) website can be viewed at www.tryorlent.example Vision statement - We enable people and communities to build and maintain strong and lasting global connections This is the brand image that we are trying to get across: •Quality—Orlent delivers the highest quality connections wherever you need to communicate. •Service—Orlent is always there for you, with the industry-leading service that promises to ensure that every experience is a good one. •Value—Orlent provides the best value in the global communications market. Typical messaging: Connecting the Most Important People in the World. Focus on international communications

We want to convey our service quality and that we really care about the service we provide and our customers. We want to emphasis the international aspect of our business. We want to make it personal, but it has to relate to business as well as individuals. We want the card to be unique in design but clear enough to read. We want a business prospect as well as a regular person to look at our card and know what we do.

Target Market(s)

Consumer - multi-ethnic consumer base living in the US calling, texting and connecting with family and friends in countries around the world 2. Busine

Industry/Entity Type

Communications

Requirements
Must have
• 1. Logo must be visible (see uploaded)

2.Artist can use variations of our company colors to accent our logo:

Hex Codes:
Magenta = ab3179
Blue = 2895c0
Green = 8ebb3f

3.Must have the following slogan visible: Because clear calls connect

below are the required data fields:

Full Name: Mark Pellow
Position: Chief Financial Officer
Office: +1 571-482-3096 ext.214
Mobile: +1 571-482-3096
Fax: +1 571-482-3096
Email: MarkP@tryorlent.example
URL: www.tryorlent.example
Address:
31872 Wrenfield Lane
suite 408
Brennick, VA 22481
USA

Nice to have
• Die cut cards or uniquely shaped cards would be interesting to see but not required

```html
<!DOCTYPE html>
<html lang="en">
<head>
<meta charset="utf-8">
<title>Orlent Telecom — Business Card</title>
<link rel="stylesheet" href="https://fonts.googleapis.com/css2?family=Open+Sans:wght@700&family=Noto+Sans+Mono:wght@400&display=swap">
<style>
  :root {
    --card-dark: #1d1d1d;
    --card-mid: #2e2e2e;
    --cyan-light: #5fe2f6;
    --cyan: #2a9fcc;
    --magenta-light: #cc4da0;
    --magenta: #a7337a;
    --green-light: #a9e232;
    --green: #8cc43c;
    --text-light: #ffffff;
  }
  * { margin: 0; padding: 0; box-sizing: border-box; }
  html, body {
    width: 1200px;
    height: 696px;
    overflow: hidden;
    background: var(--card-dark);
  }
  .card {
    position: relative;
    width: 1200px;
    height: 696px;
    overflow: hidden;
    background: radial-gradient(ellipse at 60% 35%, var(--card-mid) 0%, var(--card-dark) 70%);
    font-family: "Open Sans", Arial, sans-serif;
    color: var(--text-light);
  }
  .ribbons {
    position: absolute;
    inset: 0;
    width: 1200px;
    height: 696px;
  }
  .brand {
    position: absolute;
    left: 470px;
    top: 48px;
    width: 320px;
    display: flex;
    align-items: center;
    justify-content: center;
    gap: 14px;
  }
  .brand-mark {
    width: 30px;
    height: 30px;
    background: var(--magenta);
    border-radius: 4px;
  }
  .brand-name {
    font-size: 40px;
    font-weight: 700;
    white-space: nowrap;
    letter-spacing: 0.5px;
  }
  .person {
    position: absolute;
    right: 49px;
    top: 146px;
    text-align: right;
  }
  .person-name {
    font-size: 66px;
    font-weight: 700;
    line-height: 1.1;
    margin-right: 47px;
  }
  .person-title {
    font-size: 33px;
    font-weight: 700;
    line-height: 1.3;
    margin-top: 6px;
  }
  .contact-row {
    position: absolute;
    left: 242px;
    right: 16px;
    display: flex;
    justify-content: space-between;
    align-items: center;
    font-size: 29px;
    font-weight: 700;
    height: 60px;
    white-space: nowrap;
  }
  .row-phone { top: 405px; }
  .row-online { top: 472px; font-size: 26px; }
  .row-address {
    top: 545px;
    left: 292px;
    font-size: 28px;
  }
  .slogan {
    position: absolute;
    left: 321px;
    top: 618px;
    font-family: "Noto Sans Mono", "Courier New", monospace;
    font-size: 40px;
    font-weight: 400;
    letter-spacing: 1px;
    white-space: nowrap;
  }
</style>
</head>
<body>
  <main class="card">
    <svg class="ribbons" viewBox="0 0 1200 696" aria-hidden="true">
      <defs>
        <linearGradient id="cyanFill" x1="0" y1="0" x2="0" y2="1">
          <stop offset="0" stop-color="var(--cyan-light)"/>
          <stop offset="1" stop-color="var(--cyan)"/>
        </linearGradient>
        <linearGradient id="magentaFill" x1="0" y1="0" x2="0" y2="1">
          <stop offset="0" stop-color="var(--magenta-light)"/>
          <stop offset="1" stop-color="var(--magenta)"/>
        </linearGradient>
        <linearGradient id="greenFill" x1="0" y1="0" x2="0" y2="1">
          <stop offset="0" stop-color="var(--green-light)"/>
          <stop offset="1" stop-color="var(--green)"/>
        </linearGradient>
      </defs>
      <rect class="stripe-cyan" x="106" y="0" width="67" height="405" fill="url(#cyanFill)"/>
      <rect class="stripe-magenta" x="173" y="0" width="68" height="405" fill="url(#magentaFill)"/>
      <rect class="stripe-green" x="241" y="0" width="68" height="405" fill="url(#greenFill)"/>
      <polygon class="band-cyan" points="106,405 1200,405 1200,466 167,466" fill="url(#cyanFill)"/>
      <polygon class="band-magenta" points="173,471 1200,471 1200,533 240,533" fill="url(#magentaFill)"/>
      <polygon class="band-green" points="241,544 1200,544 1200,606 301,606" fill="url(#greenFill)"/>
    </svg>

    <div class="brand">
      <span class="brand-mark"></span>
      <span class="brand-name">Orlent Telecom</span>
    </div>

    <div class="person">
      <h1 class="person-name">Mark Pellow</h1>
      <p class="person-title">Chief Financial Officer</p>
    </div>

    <div class="contact-row row-phone">
      <span class="contact-tel">tel: +1 571-482-3096</span>
      <span class="contact-fax">fax: +1 571-482-3096</span>
    </div>
    <div class="contact-row row-online">
      <span class="contact-email">e-mail: MarkP@tryorlent.example</span>
      <span class="contact-web">web: www.tryorlent.example</span>
    </div>
    <div class="contact-row row-address">
      <span class="contact-address">31872 Wrenfield Lane suite 408 Brennick, VA 22481, USA</span>
    </div>

    <p class="slogan">Because clear calls connect</p>
  </main>
</body>
</html>
```